lantern institute of business and technology web site

I need web site for the institute which focus on business courses and computer course it is also for vocation train for employment It is also carear development and advancement .It should have links to online study resource which free
Industry/Entity Type
Business
Number of Pages Required
1 page
Look and feel

```html
<!DOCTYPE html>
<html lang="en">
<head>
<meta charset="utf-8">
<title>Lantern Institute of Business and Technology</title>
<link href="https://fonts.googleapis.com/css2?family=Open+Sans:wght@400;600;700;800&display=swap" rel="stylesheet">
<style>
:root{
  --blue:#1d63b0;
  --blue-dark:#154d8c;
  --ink:#333a40;
  --muted:#6d747a;
  --light:#f1f2f3;
  --line:#d9dcdf;
  --footer:#3a4752;
  --footer-dark:#2f3b45;
  --green:#8cc63f;
  --yellow:#f6b913;
  --white:#ffffff;
}
*{box-sizing:border-box;margin:0;padding:0}
html,body{width:1200px;height:3100px;overflow:hidden}
body{font-family:"Open Sans",Arial,sans-serif;color:var(--ink);background:var(--white);position:relative}
.wrap{width:1100px;margin:0 auto;position:relative}

/* header */
.site-header{height:160px;border-bottom:4px solid var(--blue);position:relative}
.brand{position:absolute;left:50px;top:18px;display:flex;align-items:center;gap:14px}
.brand-mark{width:70px;height:70px;background:var(--blue);border-radius:4px}
.brand-name{font-weight:800;color:var(--blue);font-size:22px;line-height:26px;text-transform:uppercase;width:320px}
.topbar{position:absolute;right:50px;top:14px;display:flex;align-items:center;gap:26px;font-size:13px}
.contact-item{display:flex;align-items:center;gap:8px}
.contact-item .label{font-weight:700;color:var(--blue);font-size:13px}
.contact-item .value{display:block;font-size:13px;color:var(--ink)}
.socials{display:flex;gap:6px}
.socials span{width:22px;height:22px;border-radius:50%;background:var(--blue);display:block}
.search{position:absolute;right:50px;top:48px;width:240px;height:28px;border:1px solid var(--line);font-size:12px;color:#999;padding:5px 10px}
.search svg{position:absolute;right:8px;top:6px}
.main-nav{position:absolute;right:50px;bottom:8px;display:flex;gap:0}
.main-nav a{display:block;padding:8px 14px;font-weight:700;font-size:14px;color:var(--ink);text-decoration:none}
.main-nav a.active{background:var(--blue);color:var(--white)}

/* hero */
.hero{height:330px;margin:10px 50px 0;position:relative;background:linear-gradient(100deg,#9aa7b1 0%,#c8cfd4 45%,#e3e6e8 70%,#b7bec4 100%)}
.hero-copy{position:absolute;left:60px;top:60px;color:var(--white)}
.hero-copy h1{font-size:44px;font-weight:800;line-height:50px;width:520px;text-shadow:0 1px 2px rgba(0,0,0,.2)}
.hero-copy p{font-size:15px;font-weight:700;width:400px;margin-top:12px;line-height:20px}
.btn-learn{display:inline-block;margin-top:28px;background:var(--blue);color:var(--white);font-weight:700;font-size:13px;padding:10px 18px}
.slide-arrow{position:absolute;top:150px;width:30px;height:40px;background:var(--blue-dark);display:flex;align-items:center;justify-content:center}
.slide-arrow.prev{left:0}.slide-arrow.next{right:0}

/* welcome */
.welcome{display:flex;justify-content:space-between;margin:170px 50px 0}
.welcome-text{width:720px}
.welcome-text h2{font-size:20px;font-weight:800;color:var(--blue);line-height:24px;text-transform:uppercase}
.welcome-text p{font-size:13px;line-height:21px;color:var(--muted);margin-top:14px}
.featured{width:320px}
.featured h3{font-size:17px;font-weight:800;border-bottom:2px solid var(--line);padding-bottom:8px}
.video{height:150px;margin-top:14px;background:linear-gradient(135deg,#6f8aa3,#b8c6d2);position:relative}
.video .play{position:absolute;left:130px;top:45px;width:60px;height:60px;border-radius:50%;background:var(--blue);display:flex;align-items:center;justify-content:center}
.featured p{font-size:12px;color:var(--muted);margin-top:10px;line-height:18px}

/* programs */
.programs{margin:110px 50px 0}
.section-head{display:flex;justify-content:space-between;align-items:center;border-bottom:2px solid var(--line);padding-bottom:8px}
.section-head h2{font-size:18px;font-weight:800;text-transform:uppercase}
.carousel-ctrl{display:flex;gap:10px}
.cards{display:flex;gap:20px;margin-top:14px}
.card{width:260px;height:300px;background:var(--light);position:relative;padding:14px}
.card h4{font-size:14px;font-weight:700;line-height:18px;height:36px}
.card .thumb{height:130px;margin-top:8px}
.card p{font-size:11.5px;color:var(--muted);line-height:17px;margin-top:10px}
.card .corner{position:absolute;right:0;bottom:0;width:0;height:0;border-left:26px solid transparent;border-bottom:26px solid var(--blue)}

/* study banner */
.study-banner{height:490px;margin-top:70px;position:relative;background:linear-gradient(90deg,#d8d2c6 0%,#ece8e0 40%,#f5f2ec 65%,#d9d3c7 100%)}
.study-copy{position:absolute;left:90px;top:160px}
.study-copy h2{font-size:62px;font-weight:800;line-height:60px;color:var(--ink)}
.study-copy h3{font-size:34px;font-weight:700;color:var(--ink);margin-top:8px}
.study-copy h3 b{color:var(--blue);font-weight:800}
.btn-click{display:inline-block;margin-top:18px;background:var(--yellow);color:var(--white);font-weight:800;font-size:26px;padding:10px 36px;border-radius:24px}

/* lower */
.lower{display:flex;justify-content:space-between;margin:60px 50px 0}
.lower-left{width:600px}
.say{text-align:center}
.say h2{font-size:17px;font-weight:800;text-transform:uppercase}
.quote-mark{width:54px;height:54px;border-radius:50%;background:var(--blue);margin:18px auto 0;display:flex;align-items:center;justify-content:center;color:var(--white);font-size:40px;font-weight:800;line-height:54px}
.say p{font-size:13px;color:var(--muted);line-height:21px;margin:18px 30px 0;font-style:normal}
.author{display:flex;justify-content:center;align-items:center;gap:10px;margin-top:14px}
.avatar{width:40px;height:40px;border-radius:50%;background:#c9b6a8}
.author b{display:block;font-size:12px}
.author span{font-size:11px;color:var(--muted)}
.alerts{margin-top:50px;background:var(--light);padding:26px 40px;text-align:center;height:180px}
.alerts h2{font-size:20px;font-weight:800;color:var(--blue);text-transform:uppercase}
.alerts p{font-size:12px;color:var(--muted);margin-top:6px}
.subscribe{display:flex;justify-content:center;margin-top:20px}
.subscribe .field{width:300px;height:36px;background:var(--white);border:1px solid var(--line);font-size:12px;color:#999;padding:9px 12px;text-align:left}
.subscribe .go{background:var(--blue);color:var(--white);font-weight:700;font-size:13px;padding:9px 16px}
.ask{width:420px;background:var(--blue);padding:22px 26px;height:600px}
.ask h2{color:var(--white);font-size:20px;font-weight:800;text-align:center;text-transform:uppercase}
.ask label{display:block;color:var(--white);font-size:12px;font-weight:700;margin-top:14px}
.ask .row{display:flex;gap:10px;margin-top:6px}
.ask .input{height:36px;background:var(--white);font-size:12px;color:#999;padding:9px 10px;flex:1}
.ask .full{margin-top:6px}
.ask .area{height:110px}
.ask .submit{margin-top:26px;background:var(--green);color:var(--white);font-size:20px;font-weight:800;text-align:center;padding:10px}

/* footer */
.site-footer{position:absolute;left:0;top:2610px;width:1200px;height:490px;background:var(--footer);color:#cfd6dc}
.foot-cols{display:flex;padding:44px 50px 0;gap:40px}
.foot-col{width:240px}
.foot-col h4{color:var(--white);font-size:14px;font-weight:800;text-transform:uppercase;margin-bottom:14px}
.foot-col li{list-style:none;font-size:12px;line-height:22px}
.news li{margin-bottom:8px;line-height:17px}
.news li small{display:block;color:#9aa6b0;font-size:11px}
.partner{position:absolute;left:50px;top:310px;display:flex;align-items:center;gap:16px}
.partner span{color:var(--white);font-weight:800;font-size:14px;line-height:18px;text-transform:uppercase}
.partner-badge{width:150px;height:70px;background:#1b1f23}
.foot-social{position:absolute;right:50px;top:330px;display:flex;gap:6px}
.foot-social span{width:24px;height:24px;border-radius:50%;background:#5a6873;display:block}
.copyright{position:absolute;left:0;bottom:0;width:1200px;height:50px;background:var(--footer-dark);font-size:12px;color:#9aa6b0;text-align:right;padding:17px 50px}
</style>
</head>
<body>

<header class="site-header">
  <div class="brand">
    <div class="brand-mark"></div>
    <div class="brand-name">Lantern Institute of Business and Technology</div>
  </div>
  <div class="topbar">
    <div class="contact-item">
      <svg width="22" height="22" viewBox="0 0 22 22"><circle cx="11" cy="11" r="11" fill="#1d63b0"/><path d="M7 6l3 0 1 3-1.5 1a6 6 0 0 0 3 3L14 11.5l3 1v3a1 1 0 0 1-1 1A10 10 0 0 1 6 7a1 1 0 0 1 1-1z" fill="#fff"/></svg>
      <div><span class="label">CALL US</span><span class="value">+260 211 555 014</span></div>
    </div>
    <div class="contact-item">
      <svg width="22" height="22" viewBox="0 0 22 22"><circle cx="11" cy="11" r="11" fill="#1d63b0"/><rect x="5.5" y="7" width="11" height="8" fill="#fff"/><path d="M5.5 7l5.5 4.5L16.5 7" stroke="#1d63b0" fill="none"/></svg>
      <div><span class="label">EMAIL US</span><span class="value">info@lanternedu.example</span></div>
    </div>
    <div class="socials"><span></span><span></span><span></span><span></span></div>
  </div>
  <div class="search">Search
    <svg width="14" height="14" viewBox="0 0 14 14"><circle cx="6" cy="6" r="4.5" stroke="#888" stroke-width="1.6" fill="none"/><path d="M9.5 9.5L13 13" stroke="#888" stroke-width="1.6"/></svg>
  </div>
  <nav class="main-nav">
    <a class="active" href="#">HOME</a><a href="#">ABOUT US</a><a href="#">COURSES</a><a href="#">CONTACT US</a>
  </nav>
</header>

<section class="hero" role="img" aria-label="Desk with tablet, laptop and notebook for study">
  <div class="hero-copy">
    <h1>LOREM IPSUM DOLOR SIT AMET</h1>
    <p>LOREM IPSUM DOLOR SIT AMET, CONSECTETUR ADIPISCING ELIT, SED DO EIUSMOD TEMPOR</p>
    <span class="btn-learn">LEARN MORE</span>
  </div>
  <div class="slide-arrow prev"><svg width="10" height="16"><path d="M8 2L2 8l6 6" stroke="#fff" stroke-width="2" fill="none"/></svg></div>
  <div class="slide-arrow next"><svg width="10" height="16"><path d="M2 2l6 6-6 6" stroke="#fff" stroke-width="2" fill="none"/></svg></div>
</section>

<section class="welcome">
  <div class="welcome-text">
    <h2>Welcome to<br>Lantern Institute of Business and Technology</h2>
    <p>Lantern Institute of Business and Technology is a fast growing education and training provider focusing on business, computer and vocational skills that lead to employment. We offer career development and advancement through flexible courses, practical workshops and distance learning. Our programmes prepare students to meet the demands of modern industry with confidence, discipline and the ability to keep learning. The institute is registered with the national vocational training authority and works closely with employers to match skills to real jobs.</p>
  </div>
  <aside class="featured">
    <h3>FEATURED VIDEO</h3>
    <div class="video" role="img" aria-label="Video still of a student at a laptop">
      <div class="play"><svg width="22" height="24"><path d="M4 2l16 10-16 10z" fill="#fff"/></svg></div>
    </div>
    <p>Lorem ipsum dolor sit amet, consectetur adipiscing elit.</p>
  </aside>
</section>

<section class="programs">
  <div class="section-head">
    <h2>Programs Offered</h2>
    <div class="carousel-ctrl">
      <svg width="10" height="14"><path d="M8 2L3 7l5 5" stroke="#333" stroke-width="2" fill="none"/></svg>
      <svg width="10" height="14"><path d="M2 2l5 5-5 5" stroke="#333" stroke-width="2" fill="none"/></svg>
    </div>
  </div>
  <div class="cards">
    <article class="card"><h4>University Education – Long Distance Learning</h4><div class="thumb" role="img" aria-label="Student studying at a laptop" style="background:linear-gradient(135deg,#7d8f9c,#c4ccd2)"></div><p>Lorem ipsum dolor sit amet, consectetur adipiscing elit, sed do eiusmod tempor incididunt ut labore et dolore magna aliqua.</p><span class="corner"></span></article>
    <article class="card"><h4>Modular Soft Skills</h4><div class="thumb" role="img" aria-label="Group discussion in a classroom" style="background:linear-gradient(135deg,#8a8f94,#d0d3d6)"></div><p>Lorem ipsum dolor sit amet, consectetur adipiscing elit, sed do eiusmod tempor incididunt ut labore et dolore magna aliqua.</p><span class="corner"></span></article>
    <article class="card"><h4>Direct to Employment (D2E)</h4><div class="thumb" role="img" aria-label="Hands working with charts and papers" style="background:linear-gradient(135deg,#5f86ad,#bcd0e2)"></div><p>Lorem ipsum dolor sit amet, consectetur adipiscing elit, sed do eiusmod tempor incididunt ut labore et dolore magna aliqua.</p><span class="corner"></span></article>
    <article class="card"><h4>Brightpath</h4><div class="thumb" role="img" aria-label="Professional in an office setting" style="background:linear-gradient(135deg,#6b7782,#c7ccd1)"></div><p>Lorem ipsum dolor sit amet, consectetur adipiscing elit, sed do eiusmod tempor incididunt ut labore et dolore magna aliqua.</p><span class="corner"></span></article>
  </div>
</section>

<section class="study-banner" role="img" aria-label="Wooden desk with laptop, lamp and books">
  <div class="study-copy">
    <h2>ONLINE STUDY</h2>
    <h3>RESOURCE WHICH <b>FREE</b></h3>
    <span class="btn-click">CLICK HERE</span>
  </div>
</section>

<section class="lower">
  <div class="lower-left">
    <div class="say">
      <h2>What Our People Say</h2>
      <div class="quote-mark">“</div>
      <p>“Lorem ipsum dolor sit amet, consectetur adipiscing elit, sed do eiusmod tempor incididunt ut labore et dolore magna aliqua. Ut enim ad minim veniam, quis nostrud exercitation ullamco laboris nisi ut aliquip ex ea commodo consequat.”</p>
      <div class="author"><div class="avatar" role="img" aria-label="Student portrait"></div><div><b>Nora Hale</b><span>Lorem ipsum</span></div></div>
    </div>
    <div class="alerts">
      <h2>Auction Alerts!</h2>
      <p>Sign up to receive email alerts about our upcoming auctions</p>
      <div class="subscribe"><div class="field">Enter your email address</div><div class="go">Subscribe</div></div>
    </div>
  </div>
  <form class="ask">
    <h2>Do You Have a Question?</h2>
    <label>Your Name*</label>
    <div class="row"><div class="input">First Name</div><div class="input">Last Name</div></div>
    <label>Email*</label>
    <div class="input full">Your Email Address here</div>
    <label>Phone</label>
    <div class="input full">Phone Number</div>
    <label>Comments*</label>
    <div class="input full area"></div>
    <div class="submit">SUBMIT</div>
  </form>
</section>

<footer class="site-footer">
  <div class="foot-cols">
    <div class="foot-col"><h4>Navigation</h4><ul><li>Home</li><li>About Us</li><li>Courses</li><li>Contact Us</li></ul></div>
    <div class="foot-col"><h4>Programs Offered</h4><ul><li>University Education – Long Distance Learning</li><li>Modular Soft Skills</li><li>Direct to Employment (D2E)</li><li>Brightpath</li><li>Study Skills Online</li><li>Career Advancement</li><li>Business Management</li><li>Technology Training</li></ul></div>
    <div class="foot-col news"><h4>Recent News</h4><ul><li><small>October 12, 2024</small>New computer lab opens for evening classes</li><li><small>September 28, 2024</small>Enrolment open for business diploma intake</li><li><small>September 10, 2024</small>Graduates placed with local employers</li></ul></div>
    <div class="foot-col"><h4>Contact Info</h4><ul><li>14 Market Road, Riverside Park, Kalema</li><li>Phone: +260 211 555 014</li><li>Mobile: +260 977 555 208</li><li>info@lanternedu.example</li></ul></div>
  </div>
  <div class="partner"><span>In Conjunction<br>With Brightpath</span><div class="partner-badge"></div></div>
  <div class="foot-social"><span></span><span></span><span></span><span></span></div>
  <div class="copyright">© 2024 Lantern Institute of Business and Technology. All Rights Reserved.</div>
</footer>

</body>
</html>
```